Mental Health Non-profit Website that takes donations

We are a faith friendly non profit mental health agency. We need an about us section, a section for taking donations, and a place to list all our therapists and a photo of them
Unfortunately, many of our neighbors in Ohio face mental health challenges which harm their quality of life. Thousands of Ohioans experience trauma, addiction, anxiety, and depression, and the negative outcomes of these experiences continue to grow. While we know that data-driven counseling can improve quality of life for those with mental health challenges, many face economic and social barriers to accessing this transformational care.
Lanterns of Calm crosses barriers to mental health care for Ohioans. We are a nonprofit team of counselors dedicated to employing best practices in modes accessible to people of all backgrounds. A trauma-informed, faith-sensitive methodology uniquely equips us to address holistic mental health challenges. Donor support and community partnerships allow us to meet and serve individuals who could not otherwise access professional care.

Please see our case for support below for more information.

Target Market(s)

Those seeking mental health therapy

Industry/Entity Type

Mental Health Non-profit

Coding

Coded - Design and coding required

Colors

Designer to choose colors to be used in the design.

Requirements
Must have
• Our logo colors of navy blue and gold, our logo, about us section, our mission section, a place to accept donations page for all of our therapists and their pictures, and a place for blog posts

```html
<!DOCTYPE html>
<html lang="en">
<head>
<meta charset="utf-8">
<title>Lanterns of Calm Behavioral Health</title>
<link href="https://fonts.googleapis.com/css2?family=Outfit:wght@400;500;600;700&display=swap" rel="stylesheet">
<style>
:root{
  --navy:#0c1340;
  --navy-deep:#070b26;
  --gold:#c9a23f;
  --gold-soft:#e7cf8a;
  --gold-line:#dcc283;
  --ink:#1b1f2e;
  --white:#ffffff;
}
*{box-sizing:border-box;margin:0;padding:0}
html,body{width:1200px;height:4295px;overflow:hidden;background:var(--white);font-family:'Outfit',sans-serif;color:var(--ink)}
.page{position:relative;width:1200px;height:4295px}
.abs{position:absolute}

/* header + hero */
.hero{position:absolute;left:0;top:0;width:1200px;height:680px;
  background:linear-gradient(180deg,#02030a 0%,#0b1433 35%,#14254f 60%,#1c2b45 85%,#2b3523 100%);
  clip-path:path("M0 0 H1200 V560 Q600 790 0 560 Z")}
.hero-dock{position:absolute;left:520px;top:160px;width:180px;height:520px;
  background:linear-gradient(180deg,rgba(120,110,100,.15),rgba(150,135,115,.55));clip-path:polygon(44% 0,56% 0,100% 100%,0 100%)}
.brand{position:absolute;left:140px;top:108px;width:160px;color:var(--gold);font-weight:600;font-size:16px;line-height:1.1;text-align:center}
.brand small{display:block;font-size:9px;letter-spacing:3px;font-weight:600}
.topbar{position:absolute;right:142px;top:16px;display:flex;align-items:center;gap:10px;color:var(--white);font-size:12px}
.topbar b{font-weight:600}
.dot{width:24px;height:24px;border:1.5px solid var(--white);border-radius:50%}
.nav{position:absolute;right:142px;top:60px;display:flex;align-items:center;gap:32px;color:var(--white);font-size:13px}
.btn-gold{display:inline-block;background:linear-gradient(90deg,#f5e6b3,#d2ad52);color:var(--navy);border-radius:30px;font-size:13px;padding:13px 22px;font-weight:500}
.hero h1{position:absolute;left:142px;top:258px;color:var(--white);font-size:37px;line-height:44px;font-weight:600;letter-spacing:.5px}
.hero p{position:absolute;left:142px;top:354px;color:#e8e8ef;font-size:15px}
.hero .btn-gold{position:absolute;left:142px;top:402px;padding:12px 20px}

/* section titles */
.mark{width:32px;height:32px;border-radius:50%;background:var(--gold)}
.sec-title{position:absolute;left:0;width:1200px;text-align:center;color:var(--navy);font-size:31px;font-weight:600}
.sec-mark{position:absolute;left:584px}

/* about */
.about-label{left:142px;top:832px;color:var(--gold);font-size:17px;letter-spacing:1.5px}
.about-title{left:142px;top:858px;color:var(--navy);font-size:33px;line-height:35px;font-weight:600}
.about-body{left:142px;top:938px;width:430px;font-size:12.8px;line-height:25.5px}
.about-body p+p{margin-top:10px}
.about-photo{left:635px;top:790px;width:422px;height:452px;border-radius:50% 50% 48% 48%;background:linear-gradient(135deg,#e8e6e1,#b9b6ad 50%,#5b3f8a)}

/* cards */
.card{position:absolute;border:1.5px solid var(--gold-line);border-radius:18px;background:var(--white);text-align:center}
.card h3{font-size:16px;font-weight:600;color:var(--ink)}
.card p{font-size:12.8px;line-height:18px;color:var(--ink)}
.photo{position:absolute;border-radius:14px}
.mission-card{top:1517px;width:422px;height:405px}
.mission-card h3{position:absolute;top:250px;left:0;width:100%}
.mission-card p{position:absolute;top:278px;left:20px;right:20px}

.therapist-card{top:2210px;width:289px;height:380px}
.therapist-card h3{position:absolute;top:172px;width:100%}
.therapist-card p{position:absolute;top:205px;left:26px;right:26px}
.portrait{position:absolute;top:2138px;width:212px;height:212px;border-radius:50%;background:radial-gradient(circle at 50% 40%,#d9c2b0,#8e7464 60%,#e7e7e7 61%)}

.blog-card{top:2850px;width:281px;height:333px}
.blog-card h3{position:absolute;top:172px;width:100%}
.blog-card p{position:absolute;top:210px;left:24px;right:24px}

.arrow{position:absolute;width:36px;height:36px;border-radius:50%}
.arrow.prev{background:#d6d6d6;left:77px}
.arrow.next{background:var(--gold);left:1087px}

/* donate */
.donate{left:142px;top:3298px;width:916px;height:380px;background:var(--gold);border-radius:20px}
.donate-photo{left:628px;top:3270px;width:389px;height:432px;border-radius:26px;background:linear-gradient(160deg,#c9e8da,#bfe1d2 55%,#8a5a3c)}
.donate h2{position:absolute;left:36px;top:108px;color:var(--white);font-size:28px;line-height:34px;font-weight:600}
.donate .tag{position:absolute;left:36px;top:194px;color:var(--white);font-size:14px;font-weight:500;letter-spacing:.5px}
.donate .btn-navy{position:absolute;left:36px;top:234px;background:var(--navy);color:var(--white);font-size:13px;padding:12px 34px;border-radius:24px}

/* footer */
.footer-bg{position:absolute;left:0;top:3800px}
.foot-brand{left:140px;top:4100px;width:215px;color:var(--gold);font-size:21px;font-weight:600;text-align:center;line-height:1.1}
.foot-brand small{display:block;font-size:11px;letter-spacing:4px}
.foot-col{position:absolute;top:3977px;color:var(--white)}
.foot-col h4{font-size:15.5px;font-weight:500;letter-spacing:.5px;margin-bottom:18px}
.foot-col li{list-style:none;font-size:13px;margin-bottom:15px;display:flex;align-items:center;gap:10px}
.foot-col .ring{width:26px;height:26px;border:1.5px solid var(--white);border-radius:50%;display:inline-block}
.foot-col .contact li{align-items:flex-start;line-height:21px;margin-bottom:10px}
.foot-rule{left:0;top:4240px;width:1200px;height:1px;background:rgba(255,255,255,.2)}
.foot-bottom{left:142px;right:142px;top:4258px;display:flex;justify-content:space-between;color:var(--white);font-size:12px}
</style>
</head>
<body>
<div class="page">

  <header class="hero">
    <div class="hero-dock" role="img" aria-label="Wooden dock stretching into a calm lake at dusk"></div>
    <div class="brand">LANTERNS OF CALM<small>BEHAVIORAL HEALTH</small></div>
    <div class="topbar">
      <svg width="14" height="14" viewBox="0 0 24 24" fill="none" stroke="#fff" stroke-width="2"><path d="M5 3h4l2 5-3 2a12 12 0 0 0 6 6l2-3 5 2v4a2 2 0 0 1-2 2A17 17 0 0 1 3 5a2 2 0 0 1 2-2z"/></svg>
      <span><b>Phone:</b> +1 555-014-2270</span>
      <span class="dot"></span><span class="dot"></span><span class="dot"></span><span class="dot"></span>
    </div>
    <nav class="nav"><span>Home</span><span>About Us</span><span>Team</span><span>Blog</span><span class="btn-gold">CONTACT US</span></nav>
    <h1>A GUIDE TO BETTER<br>MENTAL HEALTH</h1>
    <p>Steps Toward Mental Health Awareness</p>
    <span class="btn-gold">CONTACT US TODAY</span>
  </header>

  <section class="about">
    <div class="abs mark" style="left:142px;top:785px"></div>
    <div class="abs about-label">About Lanterns of Calm</div>
    <h2 class="abs about-title">Compassionate Care<br>When You Need It Most</h2>
    <div class="abs about-body">
      <p>Lanterns of Calm crosses barriers to mental health care for Ohioans. We are a nonprofit team of counselors dedicated to employing best practices in modes accessible to people of all backgrounds. A trauma-informed, faith-sensitive methodology uniquely equips us to address holistic mental health challenges. Donor support and community partnerships allow us to meet and serve individuals who could not otherwise access professional care.</p>
      <p>The following narrative introduces Lanterns of Calm and shares how community members, faith communities, and fellow agencies can partner in making this impactful expansion possible.</p>
    </div>
    <div class="abs about-photo" role="img" aria-label="Counselor in a purple top talking with a young man in a bright room with plants"></div>
  </section>

  <section class="mission">
    <div class="sec-mark mark" style="top:1350px"></div>
    <h2 class="sec-title" style="top:1403px">Our Mission</h2>
    <article class="card mission-card" style="left:142px">
      <h3>Trauma-Informed</h3>
      <p>All of our counselors have experience with trauma-informed methodology and seek to understand clients' present mental health challenges through the lens of past adverse circumstances.</p>
    </article>
    <div class="photo" style="left:162px;top:1475px;width:381px;height:255px;background:linear-gradient(135deg,#dcdad6,#8a8073 60%,#3e3a35)" role="img" aria-label="Young woman sitting on stairs holding her head"></div>
    <article class="card mission-card" style="left:636px">
      <h3>Faith-Sensitive</h3>
      <p>Many individuals experiencing mental health challenges have adopted unhealthy spiritual attitudes (e.g., "God must hate me"). Our counselors are comfortable navigating these issues with clients who initiate such conversations.</p>
    </article>
    <div class="photo" style="left:656px;top:1475px;width:381px;height:255px;background:linear-gradient(135deg,#c9a77a,#e8e3dc 45%,#3f4e3f)" role="img" aria-label="Counselor holding hands with a young woman in a session"></div>
  </section>

  <section class="therapists">
    <div class="sec-mark mark" style="top:2015px"></div>
    <h2 class="sec-title" style="top:2068px">Meet Our Therapists</h2>
    <span class="arrow prev" style="top:2384px"></span>
    <span class="arrow next" style="top:2384px"></span>
    <article class="card therapist-card" style="left:142px"><h3>Name of the Person</h3><p>Lorem ipsum dolor sit amet, consectetuer adipiscing elit, sed diam nonummy nibh euismod tincidunt ut laoreet dolore magna aliquam erat volutpat. Ut wisi enim ad minim veniam, quis nostrud exerci tation ullamcorper.</p></article>
    <article class="card therapist-card" style="left:455px"><h3>Name of the Person</h3><p>Lorem ipsum dolor sit amet, consectetuer adipiscing elit, sed diam nonummy nibh euismod tincidunt ut laoreet dolore magna aliquam erat volutpat. Ut wisi enim ad minim veniam, quis nostrud exerci tation ullamcorper.</p></article>
    <article class="card therapist-card" style="left:769px"><h3>Name of the Person</h3><p>Lorem ipsum dolor sit amet, consectetuer adipiscing elit, sed diam nonummy nibh euismod tincidunt ut laoreet dolore magna aliquam erat volutpat. Ut wisi enim ad minim veniam, quis nostrud exerci tation ullamcorper.</p></article>
    <div class="portrait" style="left:180px" role="img" aria-label="Portrait photo of a therapist"></div>
    <div class="portrait" style="left:494px" role="img" aria-label="Portrait photo of a therapist"></div>
    <div class="portrait" style="left:807px" role="img" aria-label="Portrait photo of a therapist"></div>
  </section>

  <section class="blog">
    <div class="sec-mark mark" style="top:2680px"></div>
    <h2 class="sec-title" style="top:2733px">Our Blog</h2>
    <span class="arrow prev" style="top:2999px"></span>
    <span class="arrow next" style="top:2999px"></span>
    <article class="card blog-card" style="left:142px"><h3>Lorem ipsum dolor sit amet</h3><p>Lorem ipsum dolor sit amet, consectetuer adipiscing elit, sed diam nonummy nibh euismod tincidunt ut laoreet dolore magna aliquam erat volutpat.</p></article>
    <article class="card blog-card" style="left:459px"><h3>Lorem ipsum dolor sit amet</h3><p>Lorem ipsum dolor sit amet, consectetuer adipiscing elit, sed diam nonummy nibh euismod tincidunt ut laoreet dolore magna aliquam erat volutpat.</p></article>
    <article class="card blog-card" style="left:777px"><h3>Lorem ipsum dolor sit amet</h3><p>Lorem ipsum dolor sit amet, consectetuer adipiscing elit, sed diam nonummy nibh euismod tincidunt ut laoreet dolore magna aliquam erat volutpat.</p></article>
    <div class="photo" style="left:162px;top:2808px;width:240px;height:189px;background:linear-gradient(135deg,#b08a62,#e2ddd3 50%,#4a5a48)" role="img" aria-label="Therapy session with a client on a couch"></div>
    <div class="photo" style="left:479px;top:2808px;width:241px;height:189px;background:linear-gradient(135deg,#d8dcd8,#9aa79a 50%,#3b4a3b)" role="img" aria-label="Support group sitting together by a window"></div>
    <div class="photo" style="left:798px;top:2808px;width:240px;height:189px;background:linear-gradient(135deg,#8e8e8e,#c9c9c7 55%,#f0f0ee)" role="img" aria-label="Distressed client with a doctor taking notes"></div>
  </section>

  <section class="abs donate">
    <h2>Help Us Bring Hope to<br>Those Who Need It Most</h2>
    <div class="tag">Give a Little, Change a Lot</div>
    <span class="btn-navy">Donate Now</span>
  </section>
  <div class="abs donate-photo" role="img" aria-label="Two pairs of hands holding a red heart"></div>

  <footer>
    <svg class="footer-bg" width="1200" height="495" viewBox="0 0 1200 495"><path d="M0 110 Q300 30 560 17 Q590 17 600 40 Q610 17 640 17 Q900 30 1200 110 V495 H0 Z" fill="var(--navy-deep)"/></svg>
    <div class="abs foot-brand">LANTERNS OF CALM<small>BEHAVIORAL HEALTH</small></div>
    <div class="foot-col" style="left:410px"><h4>NAVIGATION BAR</h4><ul><li>» Home</li><li>» About Us</li><li>» Team</li><li>» Blog</li><li>» Contact Us</li></ul></div>
    <div class="foot-col" style="left:623px"><h4>STAY CONNECTED</h4><ul><li><span class="ring"></span>Community</li><li><span class="ring"></span>Updates</li><li><span class="ring"></span>Gallery</li><li><span class="ring"></span>Network</li></ul></div>
    <div class="foot-col" style="left:848px"><h4>CONTACT DETAILS</h4><ul class="contact">
      <li><svg width="12" height="16" viewBox="0 0 12 16"><path d="M6 0a6 6 0 0 1 6 6c0 4-6 10-6 10S0 10 0 6a6 6 0 0 1 6-6z" fill="#fff"/><circle cx="6" cy="6" r="2.2" fill="var(--navy-deep)"/></svg><span>48 Willow Lane,<br>Maple Grove, OH</span></li>
      <li><svg width="12" height="12" viewBox="0 0 24 24"><path d="M5 3h4l2 5-3 2a12 12 0 0 0 6 6l2-3 5 2v4a2 2 0 0 1-2 2A17 17 0 0 1 3 5a2 2 0 0 1 2-2z" fill="#fff"/></svg><span>Phone<br>+1 555-014-2270</span></li>
      <li><svg width="13" height="10" viewBox="0 0 13 10"><rect width="13" height="10" fill="#fff"/><path d="M0 0l6.5 5L13 0" stroke="var(--navy-deep)" fill="none"/></svg><span>Email<br>info@lanternsofcalm.org</span></li>
    </ul></div>
    <div class="abs foot-rule"></div>
    <div class="abs foot-bottom"><span>Copyright © 2024 Lanterns of Calm. All Rights Reserved.</span><span>Privacy Policy &nbsp; | &nbsp; Terms of Use</span></div>
  </footer>

</div>
</body>
</html>
```